Postcard design to acquire new clients for my Property Management Company

I'm looking for a postcard design that I can send to prospective clients detailing information about my company and services.
Postcard should be eye catching and contain information from www.brightkeyrentals-example.com. I've provided a few screen shots for the most important information and my logo.
Target Market(s)
Real Estate
Industry/Entity Type
Real Estate
Font styles to use
Sans Serif
Requirements
Must have
- Must be eye catching!! this will be a direct mail piece - I'd like for the card to be read and not tossed in the trash immediately.
Design que from the logo.
A place to write / print the receipts name and address.
our physical address - 2287 Marble Lane, Lubbock, TX 79555.
Should not have
- the contact information on the business card is not accurate - please use info from website.

```html
<!DOCTYPE html>
<html lang="en">
<head>
<meta charset="utf-8">
<title>BrightKey Property Management – Direct Mail Postcard</title>
<link href="https://fonts.googleapis.com/css2?family=Montserrat:wght@400;600;700;800;900&family=Roboto:wght@400;500;700&family=Roboto+Condensed:wght@400;700&display=swap" rel="stylesheet">
<style>
  :root{
    --canvas:#e8e9ea;
    --card-black:#141414;
    --card-charcoal:#2e2e2e;
    --white:#ffffff;
    --navy:#1d4b8a;
    --navy-deep:#17427d;
    --gold:#f3c321;
    --slate:#8c939b;
    --panel-grey:#e3e4e6;
    --rule:#8a8d90;
    --photo-dark:#2b2d2f;
    --photo-mid:#6e7276;
  }
  *{box-sizing:border-box;margin:0;padding:0}
  html,body{width:858px;height:1200px;overflow:hidden}
  body{background:var(--canvas);position:relative;font-family:"Roboto",Arial,sans-serif}

  /* ---------- FRONT ---------- */
  .postcard-front{
    position:absolute;left:42px;top:48px;width:370px;height:262px;overflow:hidden;
    background:radial-gradient(ellipse at 55% 40%,var(--card-charcoal) 0%,var(--card-black) 75%);
    color:var(--white);font-family:"Montserrat",Arial,sans-serif;
  }
  .hero-photo{
    position:absolute;right:0;top:0;width:185px;height:262px;
    background:radial-gradient(ellipse at 50% 45%,var(--photo-mid) 0%,var(--photo-dark) 70%,transparent 100%);
  }
  .brand{position:absolute;left:34px;top:12px;line-height:1}
  .brand-name{font-size:13px;font-weight:700;letter-spacing:2.2px;display:block}
  .brand-tag{font-size:5.6px;font-weight:400;letter-spacing:1.6px;display:block;margin-top:2px}
  .headline-box{
    position:absolute;left:23px;top:63px;width:155px;height:33px;
    border:1.5px solid var(--white);
    font-size:27px;font-weight:800;text-align:center;line-height:30px;letter-spacing:.5px;
  }
  .headline-sub{position:absolute;left:23px;width:155px;text-align:center;font-weight:800;line-height:1}
  .headline-sub.financial{top:99px;font-size:15.5px}
  .headline-sub.returns{top:112px;font-size:23px;letter-spacing:.5px}
  .headline-sub.support{top:144px;font-size:6.6px;font-weight:700}
  .headline-sub.specialists{top:152px;font-size:20px;letter-spacing:.6px}
  .contact-block{position:absolute;left:10px;top:189px;width:155px}
  .contact-title{
    height:22px;border:1.2px solid var(--white);
    font-size:13px;font-weight:700;text-align:center;line-height:20px;background:var(--card-black);
  }
  .contact-list{list-style:none;background:rgba(60,60,60,.55);padding:6px 6px 6px 7px;font-family:"Roboto",Arial,sans-serif;font-size:7.2px}
  .contact-list li{display:flex;align-items:center;gap:6px;height:10.5px}
  .contact-list svg{width:7px;height:7px;flex:none}

  /* ---------- BACK ---------- */
  .postcard-back{
    position:absolute;left:444px;top:161px;width:371px;height:262px;background:var(--white);
    font-family:"Roboto",Arial,sans-serif;
  }
  .services-panel{
    position:absolute;left:9px;top:11px;width:171px;height:240px;background:var(--navy-deep);
    padding:10px 6px 0 5px;color:var(--white);
  }
  .services-title{
    display:inline-block;margin-left:12px;padding:1px 4px 3px 4px;
    border-bottom:1px solid var(--gold);border-right:1px solid var(--gold);
    font-size:10.5px;font-weight:500;letter-spacing:.3px;
  }
  .service{margin-top:4.6px;font-size:4.6px;line-height:5.6px;font-family:"Roboto Condensed",Arial,sans-serif}
  .service:first-of-type{margin-top:7px}
  .service-name{color:var(--gold);font-family:"Roboto",Arial,sans-serif;font-size:7.4px;font-weight:500;margin-right:2px}

  .back-brand{position:absolute;left:194px;top:14px;line-height:1;color:var(--navy)}
  .back-brand .brand-name{font-family:"Montserrat",Arial,sans-serif;font-size:9.5px;letter-spacing:1.6px;color:var(--slate)}
  .back-brand .brand-tag{font-family:"Montserrat",Arial,sans-serif;font-size:4.2px;letter-spacing:1px;color:var(--navy)}
  .pitch{position:absolute;left:194px;top:39px;color:var(--navy);font-family:"Montserrat",Arial,sans-serif;font-weight:700;line-height:1}
  .pitch-lead{font-size:8.6px;display:flex;align-items:center;gap:2px}
  .pitch-lead svg{width:9px;height:9px}
  .pitch-main{font-size:12.5px;font-weight:800;line-height:13.5px;margin-top:2px}
  .stamp-box{position:absolute;left:302px;top:8px;width:62px;height:77px;border:1px solid var(--card-black)}
  .address-panel{position:absolute;left:194px;top:100px;width:170px;height:112px;background:var(--panel-grey)}
  .address-line{position:absolute;left:10px;width:150px;height:1px;background:var(--rule)}
  .phone{position:absolute;left:194px;top:222px;font-size:25.5px;color:var(--navy);letter-spacing:-.2px;line-height:1}
</style>
</head>
<body>

<section class="postcard-front" aria-label="Postcard front">
  <div class="hero-photo" role="img" aria-label="Photo of a property management specialist in a grey shirt, arms crossed, on a dark backdrop"></div>

  <div class="brand">
    <span class="brand-name">BRIGHTKEY</span>
    <span class="brand-tag">PROPERTY MANAGEMENT</span>
  </div>

  <div class="headline-box">MAXIMIZE</div>
  <div class="headline-sub financial">YOUR FINANCIAL</div>
  <div class="headline-sub returns">RETURNS</div>
  <div class="headline-sub support">WITH SUPPORT FROM OUR RENTAL</div>
  <div class="headline-sub specialists">SPECIALISTS</div>

  <div class="contact-block">
    <div class="contact-title">Contact Expert</div>
    <ul class="contact-list">
      <li><svg viewBox="0 0 10 10"><path d="M2 1l2 2-1 1.3c.6 1.2 1.5 2.1 2.7 2.7L7 6l2 2-1.3 1.3C4.5 9 1 5.5.7 2.3z" fill="#fff"/></svg>(806) 555 0147</li>
      <li><svg viewBox="0 0 10 10"><rect x=".7" y="2" width="8.6" height="6" fill="none" stroke="#fff" stroke-width=".9"/><path d="M.7 2L5 5.5 9.3 2" fill="none" stroke="#fff" stroke-width=".9"/></svg>info@brightkeyrentals-example.com</li>
      <li><svg viewBox="0 0 10 10"><path d="M5 .5a3.3 3.3 0 0 0-3.3 3.3C1.7 6.5 5 9.5 5 9.5s3.3-3 3.3-5.7A3.3 3.3 0 0 0 5 .5z" fill="#fff"/><circle cx="5" cy="3.8" r="1.2" fill="#333"/></svg>2287 Marble Lane, Lubbock, TX 79555</li>
    </ul>
  </div>
</section>

<section class="postcard-back" aria-label="Postcard back">
  <div class="services-panel">
    <div class="services-title">DISCOVER OUR SERVICES</div>
    <p class="service"><span class="service-name">PROPERTY MARKETING</span>Tired of waiting for weeks on end, hoping to find a new tenant? Let us take over your marketing for you and we'll find a qualified renter quickly.</p>
    <p class="service"><span class="service-name">TENANT SCREENING</span>We don't just find someone to rent your home—we find the best renters. We screen all applications using fair housing guidelines to protect you.</p>
    <p class="service"><span class="service-name">PROPERTY INSPECTIONS</span>Inspections form an important part of our proactive property management approach. We visit every home in our portfolio regularly.</p>
    <p class="service"><span class="service-name">EVICTIONS</span>When things go wrong inside your rental home, rest easy with the experts on your side. We will handle evictions for you &amp; find new renters when it's over.</p>
    <p class="service"><span class="service-name">LEGAL GUIDANCE</span>Don't accidentally violate one of the many ordinances and housing laws governing your relationship with your tenants. Let us keep you compliant.</p>
    <p class="service"><span class="service-name">RENT COLLECTION</span>Stop guessing when you'll receive your rental earnings every month and say hello to consistent payments. We keep your tenants current.</p>
    <p class="service"><span class="service-name">MAINTENANCE</span>Still scrambling to respond to repair requests every time you receive a tenant call? Let us coordinate repair work on your behalf.</p>
    <p class="service"><span class="service-name">FINANCIAL REPORTING</span>Keep a handle on your real estate performance. We generate monthly statements so you can review income &amp; expenses at a moment's notice.</p>
  </div>

  <div class="back-brand">
    <span class="brand-name">BRIGHTKEY</span>
    <span class="brand-tag">PROPERTY MANAGEMENT</span>
  </div>

  <div class="pitch">
    <div class="pitch-lead">CHOOSE THE RIGHT
      <svg viewBox="0 0 10 10"><circle cx="5" cy="5" r="5" fill="#1d4b8a"/><path d="M2.8 5.2l1.5 1.5 3-3.2" fill="none" stroke="#fff" stroke-width="1.2"/></svg>
    </div>
    <div class="pitch-main">PROPERTY<br>MANAGEMENT<br>SYSTEM</div>
  </div>

  <div class="stamp-box" aria-label="Stamp area"></div>

  <div class="address-panel" aria-label="Recipient name and address">
    <span class="address-line" style="top:32px"></span>
    <span class="address-line" style="top:56px"></span>
    <span class="address-line" style="top:80px"></span>
  </div>

  <div class="phone">(806) 555 0147</div>
</section>

</body>
</html>
```